Energy Healing for pregnant women postcard

I am an intuitive energy healer specializing in the care of pregnant women and their babies. I have an existing logo that is attached that should be placed on the card,sizing is at your discretion, recolor as needed. The message of the card should be one that conveys tranquility, growth, life and light. Images of pregnancy and motherhood could also fit well on the card, but that is not required if the preceding messages can be conveyed through other imagery. Also on the card, the following should appear: (company name and tag line)Positivity & JoyHealing the mind, body, spirit and soul with Energy provided to all living things by the Universe. Space should be left for my name and credentials on the front, while the address space on the back will be used for more contact information. Opposite the address block on the back, please leave room for a text box that will include benefits of the services. About 2"x3" should suffice.

Target Market(s)

Pregnant women and newly post-partum women

Industry/Entity Type

Health And Wellness

Font styles to use
Script

Colors
b05ba4
b768aa
d3a5cc
ecdaeb
e7f5f8
cfdeed
cee9f5
85cae6

Requirements
Must have
• Company logo. Company name. Tag line. Individual name and certifications
Nice to have
• Pictures or images that convey peace, tranquility healing and growth.
Should not have
• Anything harsh.

```html
<!DOCTYPE html>
<html lang="en">
<head>
<meta charset="utf-8">
<title>Harbor &amp; Wren — Energy Healing Postcard</title>
<link rel="stylesheet" href="https://fonts.googleapis.com/css2?family=Dancing+Script:wght@600&family=Ubuntu:ital,wght@0,400;0,500;1,400&display=swap">
<style>
  :root {
    --orchid: #b05ba4;
    --orchid-soft: #b768aa;
    --lilac: #d3a5cc;
    --blush: #ecdaeb;
    --mist: #e7f5f8;
    --sky: #cee9f5;
    --ink: #4a4a4a;
    --paper: #ffffff;
    --backdrop: #f1eef1;
  }
  * { box-sizing: border-box; margin: 0; padding: 0; }
  html, body { width: 1200px; height: 1000px; overflow: hidden; }
  body {
    background: var(--backdrop);
    font-family: "Ubuntu", sans-serif;
    position: relative;
  }

  /* ---------- Front of postcard ---------- */
  .postcard-front {
    position: absolute;
    left: 60px; top: 40px;
    width: 660px; height: 490px;
    overflow: hidden;
    box-shadow: 0 6px 18px rgba(0,0,0,.18);
  }
  .front-photo {
    position: absolute; inset: 0;
    background:
      linear-gradient(180deg, rgba(255,255,255,.0) 55%, rgba(120,95,80,.55) 100%),
      linear-gradient(100deg, #eef2f3 0%, #dfe5e2 25%, #c9b27a 42%, #e3a630 55%, #d68a1c 70%, #8a5a22 100%);
  }
  .brand-mark {
    position: absolute; left: 22px; top: 24px;
    display: flex; align-items: center; gap: 6px;
    font-family: "Ubuntu", sans-serif;
    font-size: 13px; color: #8a9a88;
  }
  .brand-mark .dot {
    width: 14px; height: 14px; border-radius: 50%;
    border: 1.5px solid #8a9a88;
  }
  .benefits-panel {
    position: absolute; top: 0; bottom: 0;
    left: 382px; width: 232px;
    background: rgba(240,238,240,.86);
    text-align: center;
    padding-top: 48px;
  }
  .brand-title {
    font-family: "Dancing Script", cursive;
    font-weight: 600;
    font-size: 40px; line-height: 1.05;
    color: var(--orchid);
  }
  .benefit-list {
    list-style: none;
    margin-top: 42px;
    font-style: italic;
    font-size: 16px; line-height: 1.32;
    color: var(--ink);
  }
  .practitioner {
    margin-top: 40px;
    font-size: 17px; font-weight: 500; line-height: 1.3;
    color: var(--orchid);
  }

  /* ---------- Back of postcard ---------- */
  .postcard-back {
    position: absolute;
    left: 580px; top: 560px;
    width: 580px; height: 410px;
    background: var(--paper);
    box-shadow: 0 6px 18px rgba(0,0,0,.18);
  }
  .info-block {
    position: absolute; left: 0; top: 0;
    width: 318px; height: 318px;
    background: var(--orchid);
    color: var(--paper);
    text-align: center;
    padding-top: 18px;
  }
  .info-block .practitioner-name {
    font-size: 17px; line-height: 1.3;
    letter-spacing: .3px;
  }
  .credentials {
    list-style: none;
    margin-top: 14px;
    font-style: italic;
    font-size: 14px; line-height: 1.4;
  }
  .credentials svg { width: 11px; height: 11px; vertical-align: -1px; margin-right: 4px; }
  .gallery {
    display: grid;
    grid-template-columns: 128px 128px;
    gap: 10px;
    justify-content: center;
    margin-top: 20px;
  }
  .gallery-tile {
    height: 80px;
    border: 3px solid var(--blush);
  }
  .tile-garden  { background: linear-gradient(135deg, #5f9a3e, #d9e9cf 60%, #e89060); }
  .tile-sofa    { background: linear-gradient(160deg, #a89c9a, #efe9e4 55%, #3f4658); }
  .tile-beach   { background: linear-gradient(180deg, #7fc3e6 0%, #cfe9f4 50%, #e8d9b7 100%); }
  .tile-meadow  { background: linear-gradient(180deg, #5c9a35 0%, #a9cf6e 55%, #f1efe6 100%); }

  .stamp-box {
    position: absolute; right: 28px; top: 24px;
    width: 62px; height: 72px;
    border: 1.5px solid #555;
  }
  .address-lines {
    position: absolute; right: 28px; top: 168px;
    width: 146px;
  }
  .address-lines span {
    display: block; height: 1.5px; background: #777;
    margin-bottom: 26px;
  }
</style>
</head>
<body>

  <section class="postcard-front">
    <div class="front-photo" role="img" aria-label="Photo of an expectant mother sitting cross-legged in meditation on a path lined with golden autumn trees"></div>

    <div class="brand-mark"><span class="dot"></span>Harbor &amp; Wren</div>

    <div class="benefits-panel">
      <h1 class="brand-title">Harbor<br>&amp; Wren</h1>
      <ul class="benefit-list">
        <li>Deep relaxation</li>
        <li>Decrease anxiety</li>
        <li>Decrease stress</li>
        <li>Decrease discomforts</li>
        <li>Promote feelings of</li>
        <li>wellbeing</li>
        <li>Promote balance</li>
        <li>Relieve physical</li>
        <li>discomforts of pregnancy</li>
      </ul>
      <p class="practitioner">Marisol K. Whitfield<br>MSN, RCMT</p>
    </div>
  </section>

  <section class="postcard-back">
    <div class="info-block">
      <p class="practitioner-name">Marisol K. Whitfield<br>MSN, RCMT</p>
      <ul class="credentials">
        <li><svg viewBox="0 0 12 12"><path d="M1.5 6.5 L4.5 9.5 L10.5 2" fill="none" stroke="#fff" stroke-width="1.6"/></svg>Reiki Master Teacher</li>
        <li><svg viewBox="0 0 12 12"><path d="M1.5 6.5 L4.5 9.5 L10.5 2" fill="none" stroke="#fff" stroke-width="1.6"/></svg>Archangelic Light Master Teacher</li>
      </ul>
      <div class="gallery">
        <div class="gallery-tile tile-garden" role="img" aria-label="Expectant mother in prayer pose on a garden lawn"></div>
        <div class="gallery-tile tile-sofa" role="img" aria-label="Expectant mother resting on a sofa"></div>
        <div class="gallery-tile tile-beach" role="img" aria-label="Expectant mother meditating on a sandy beach"></div>
        <div class="gallery-tile tile-meadow" role="img" aria-label="Expectant mother holding baby clothes in a green meadow"></div>
      </div>
    </div>

    <div class="stamp-box"></div>
    <div class="address-lines"><span></span><span></span><span></span><span></span></div>
  </section>

</body>
</html>
```